VERIX WORDPRESS DESIGN

Hello Happy People,

My name is Jai i run a company called peakmarkhub.net.au am working on a new project with LED lighting and have decided to try craft tribe as i've heard great things.

Our company is in need of wordpress design for a new company 'Verix' we wholesale the best LED lighting products in the world :)

We are targeting commercial customers, small and medium also!

I would like a wordpress design based on the logos, pictures and content that i provide.

We would like to see the design include;
home page
about us Page
Distributors Page
Lighting School Page
small medium enterprise
commercial enterprise
industrial and mining
Categories Page
Contact Us Page

5 year warranty badge included
10 year extended warranty badge included
I have put a catalogue together for the lighting products that looks better then the rubbish on the website.

We will be on linkedin & facebook

Our company website is www.verix.com.au

I am available for the next 10 days to go through with anyone that is interested in taking this project on and will offer work

Industry/Entity Type

School

Requirements
Must have
• banners with factories and commercial lighting products depending on the page

```html
<!DOCTYPE html>
<html lang="en">
<head>
<meta charset="utf-8">
<title>Verix – LED Lighting</title>
<link href="https://fonts.googleapis.com/css2?family=Oswald:wght@300;400;500&family=PT+Sans:wght@400;700&display=swap" rel="stylesheet">
<style>
:root{
  --black:#000;
  --ink:#111;
  --page:#f4f4f4;
  --green:#1e9a3f;
  --rule:#d6d6d6;
  --white:#fff;
  --muted:#9a9a9a;
}
*{margin:0;padding:0;box-sizing:border-box}
html,body{width:1064px;height:1200px;overflow:hidden}
body{background:var(--page);font-family:"PT Sans",sans-serif;color:var(--ink);position:relative}
.header{position:absolute;left:0;top:0;width:1064px;height:90px;background:var(--black)}
.brand{position:absolute;color:var(--white);text-align:center;font-family:"PT Sans",sans-serif}
.brand-name{display:block;font-size:46px;line-height:44px;font-weight:400;letter-spacing:1px}
.brand-url{display:block;font-size:13px;letter-spacing:1.5px;line-height:14px}
.header .brand{left:192px;top:8px;width:150px}
.social{position:absolute;top:27px;width:24px;height:24px;border-radius:50%;background:#3d5a80;box-shadow:0 1px 2px rgba(255,255,255,.3) inset}
.social.one{left:649px}
.social.two{left:679px;background:#4a7b9a}
.search{position:absolute;left:731px;top:29px;width:142px;height:21px;background:var(--white);border:1px solid #ccc;font-size:11px;padding:3px 0 0 7px;color:#222}
.search-btn{position:absolute;right:2px;top:2px;width:17px;height:16px;background:var(--black)}
.nav{position:absolute;left:184px;top:81px;width:696px;height:37px;background:var(--black);border:2px solid var(--white);border-top-width:2px;border-radius:4px;display:flex;align-items:center;padding-left:12px;gap:0}
.nav a{font-family:"Oswald",sans-serif;font-size:10.5px;color:var(--white);text-decoration:none;padding:3px 6px;line-height:12px;letter-spacing:-.1px}
.nav a.active{background:var(--green)}
.rule{position:absolute;left:90px;width:884px;height:1px;background:var(--rule)}
.hero{position:absolute;left:184px;top:168px;width:696px;height:299px;border:3px solid var(--black);background:linear-gradient(160deg,#c9d9ea 0%,#b3c5d8 35%,#6b6a62 60%,#3b3f45 100%)}
.hero-text{position:absolute;left:27px;top:26px;font-family:"Oswald",sans-serif;color:var(--ink)}
.hero-title{font-size:34px;line-height:40px;font-weight:300}
.hero-title b{font-weight:500}
.hero-sub{font-size:28px;line-height:34px;font-weight:300}
.hero-cta{font-size:34px;line-height:40px;font-weight:500;color:var(--green)}
.dots{position:absolute;left:508px;top:484px;display:flex;gap:3px}
.dots span{width:10px;height:10px;border-radius:50%;background:#ddd;border:1px solid #999}
.dots span.on{background:#555}
.section-title{position:absolute;left:0;width:1064px;text-align:center;font-family:"Oswald",sans-serif;font-size:31px;font-weight:400;line-height:36px}
.product{position:absolute;width:112px;height:112px}
.product-photo{position:absolute;inset:0;border-radius:50%;border:3px solid var(--black);background:radial-gradient(circle at 50% 40%,#fff 0%,#e6e6e6 55%,#cfcfcf 100%)}
.product-code{position:absolute;left:50%;top:74px;transform:translateX(-50%);background:var(--black);color:var(--white);font-family:"Oswald",sans-serif;font-size:16px;line-height:28px;padding:0 8px;white-space:nowrap;letter-spacing:-.3px}
.pager{position:absolute;left:466px;top:848px;display:flex;align-items:center;gap:6px;font-family:"Oswald",sans-serif;font-size:11px;color:var(--muted)}
.pager .arrow,.pager .current{width:17px;height:17px;border-radius:50%;background:var(--black);color:var(--white);display:flex;align-items:center;justify-content:center}
.pager span{min-width:10px;text-align:center}
.cat-col{position:absolute;top:971px;list-style:none;font-size:11.5px;line-height:19.7px}
.cat-col li{padding-left:14px;position:relative}
.cat-col li::before{content:"»";position:absolute;left:0;top:0;font-weight:700}
.footer{position:absolute;left:0;top:1081px;width:1064px;height:119px;background:var(--black)}
.footer-nav{position:absolute;top:17px;left:0;width:1064px;text-align:center;font-size:8.3px;color:var(--white);word-spacing:0}
.footer-nav a{color:var(--white);text-decoration:none;margin:0 5.5px}
.footer .brand{left:457px;top:43px;width:150px}
.footer .brand-name{font-size:38px;line-height:36px}
.footer .brand-url{font-size:11px}
.copyright{position:absolute;top:91px;left:0;width:1064px;text-align:center;color:var(--white);font-size:9.5px;font-weight:700}
</style>
</head>
<body>
<header class="header">
  <div class="brand"><span class="brand-name">Verix</span><span class="brand-url">www.verix.com.au</span></div>
  <span class="social one" aria-label="Social profile"></span>
  <span class="social two" aria-label="Social profile"></span>
  <div class="search">Search
    <span class="search-btn"><svg width="17" height="16" viewBox="0 0 17 16"><circle cx="7.5" cy="7" r="3.5" fill="none" stroke="#fff" stroke-width="1.6"/><line x1="10" y1="9.5" x2="13" y2="12.5" stroke="#fff" stroke-width="1.8"/></svg></span>
  </div>
</header>
<nav class="nav">
  <a class="active">HOME</a><a>ABOUT US</a><a>DISTRIBUTORS</a><a>LIGHTING SCHOOL</a><a>SMALL MEDIUM ENTERPRISE</a><a>COMMERCIAL ENTERPRISE</a><a>INDUSTRIAL AND MINING</a><a>CATEGORIES</a><a>CONTACT US</a>
</nav>
<div class="rule" style="top:137px"></div>
<section class="hero" role="img" aria-label="Photo of glass office towers against a blue sky">
  <div class="hero-text">
    <div class="hero-title"><b>LED</b> DOWN LIGHTS</div>
    <div class="hero-sub">See our range</div>
    <div class="hero-cta">Click Here</div>
  </div>
</section>
<div class="dots"><span></span><span class="on"></span><span></span><span></span></div>
<div class="rule" style="top:521px"></div>
<h2 class="section-title" style="top:536px">FEATURED</h2>
<div class="product" style="left:192px;top:581px"><div class="product-photo" role="img" aria-label="Portable work floodlight"></div><div class="product-code">VRX5-DL-4K</div></div>
<div class="product" style="left:382px;top:581px"><div class="product-photo" role="img" aria-label="LED driver unit"></div><div class="product-code">VRX8-CL-85-5K</div></div>
<div class="product" style="left:571px;top:581px"><div class="product-photo" role="img" aria-label="Track spotlight"></div><div class="product-code">VRX8-CL-85-5K</div></div>
<div class="product" style="left:761px;top:581px"><div class="product-photo" role="img" aria-label="LED globe"></div><div class="product-code">VRX8-CL-85-5K</div></div>
<div class="product" style="left:192px;top:707px"><div class="product-photo" role="img" aria-label="High bay LED light"></div><div class="product-code">VRX5-DL-4K</div></div>
<div class="product" style="left:382px;top:707px"><div class="product-photo" role="img" aria-label="LED down light"></div><div class="product-code">VRX8-CL-85-5K</div></div>
<div class="product" style="left:571px;top:707px"><div class="product-photo" role="img" aria-label="COB down light"></div><div class="product-code">VRX8-CL-85-5K</div></div>
<div class="product" style="left:761px;top:707px"><div class="product-photo" role="img" aria-label="LED flood light"></div><div class="product-code">VRX8-CL-85-5K</div></div>
<div class="pager">
  <span class="arrow"><svg width="9" height="9" viewBox="0 0 9 9"><path d="M5 1L2 4.5L5 8M8 1L5 4.5L8 8" fill="none" stroke="#fff" stroke-width="1.2"/></svg></span>
  <span>1</span><span>2</span><span>3</span><span class="current">4</span><span>5</span><span>6</span>
  <span class="arrow"><svg width="9" height="9" viewBox="0 0 9 9"><path d="M4 1L7 4.5L4 8M1 1L4 4.5L1 8" fill="none" stroke="#fff" stroke-width="1.2"/></svg></span>
</div>
<div class="rule" style="top:894px"></div>
<h2 class="section-title" style="top:919px">CATEGORIES</h2>
<ul class="cat-col" style="left:192px"><li>MR16</li><li>Ceiling Lights</li><li>Down Lights</li><li>EXIT &amp; Emergency Lighting</li></ul>
<ul class="cat-col" style="left:361px"><li>LED Globes</li><li>Candle</li><li>Candle Fancy</li><li>High Bay Lighting</li></ul>
<ul class="cat-col" style="left:538px"><li>Low Bay Lighting</li><li>Panel Lighting</li><li>PAR Lighting</li><li>Sensor Light</li></ul>
<ul class="cat-col" style="left:714px"><li>Track Lighting</li><li>Tubular Lighting</li><li>Work Lighting</li></ul>
<footer class="footer">
  <div class="footer-nav"><a>HOME</a><a>ABOUT US</a><a>DISTRIBUTORS</a><a>LIGHTING SCHOOL</a><a>SMALL MEDIUM ENTERPRISE</a><a>COMMERCIAL ENTERPRISE</a><a>INDUSTRIAL AND MINING</a><a>CATEGORIES</a><a>CONTACT US</a></div>
  <div class="brand"><span class="brand-name">Verix</span><span class="brand-url">www.verix.com.au</span></div>
  <div class="copyright">© 2012 Verix</div>
</footer>
</body>
</html>
```